Buchcover-Design für Fachbuch
Tolle Entwürfe und ein sehr effiziente Zusammenarbeit. Können wir nur weiterempfehlen.
Zielgruppe
Unternehmensberatung im Thema Arbeitszeit. Wir haben ein Fachbuch zum Thema Arbeitszeit und Personaleinsatzplanung für Geschäftsführer, HR Mitarbeiter, Führungskräfte, Studenten und alle geschrieben, die sich o.g. Themen näher informieren möchten
Aufgabenstellung
Folgende Textelemente sollen zu sehen sein:
Autorennamen: Dr. Reinhold Kattner, Lothar Brenning
Titel: PLAN STARK Betrieb - Dienstzeiten und Schichtorganisation fair, rentabel und marktnah einrichten
Außerdem: Unter Mitwirkung von Prof. Anton K. Ruhland
Und: mit vielen Praxisbeispielen (ggf. als eine Art Plakette)
Auf der Rückseite soll ein Klappentext und 2 Zitate zu sehen sein:
Klappentext:
Die Welt verändert sich dramatisch. Digitalisierung, Fachkräftemangel, Wertewandel und nicht zuletzt Ausnahmezustände wie die Coronakrise stellen Unternehmen vor große Herausforderungen. Wie können Unternehmen flexibel und gleichzeitig wirtschaftlich, kunden- und mitarbeiterorientiert agieren?
Reinhold Kattner und Lothar Brenning sehen eine innovative Arbeitszeitgestaltung als entscheidenden Hebel an, um Unternehmen aller Branchen in schnelllebigen Märkten flexibel aufzustellen. Die Autoren beleuchten mit vielen Beispielen aus ihrer Beratungspraxis, warum Arbeitszeitsysteme dringend modernisiert werden müssen und welche Möglichkeiten Sie bereits heute haben, Arbeitszeit innovativ zu gestalten.
Sie erfahren alles Wissenswerte über klassische Modelle, wie z.B. Schichtplan, Gleitzeit, Vertrauensarbeitszeit, Zeitkontensystem und Teilzeit, über Workforce Management (Workforce Analytics, Personalbedarfsermittlung und Forecast, Personaleinsatzplanung, Zeiterfassung) bis hin zu Lebensarbeitszeit, Gruppenarbeit, Selbstorganisation, Homeoffice und New Work. Dabei lernen Sie nicht nur die Einzelkomponenten kennen, sondern erfahren auch, wie man diese geschickt zu einer für Mitarbeiter und Unternehmen gleichermaßen vorteilhaften Arbeitszeitsystematik kombiniert. Neben diesem strategischen Wissen vermitteln Ihnen die Autoren hilfreiche Methoden zur konkreten operativen Umsetzung dieser Themen.
Zitat 1:
„Durch die Weitergabe ihrer umfassenden Erfahrungen aus der Beratung ist es den Autoren in hervorragender Weise gelu..

```html
<!DOCTYPE html>
<html lang="de">
<head>
<meta charset="utf-8">
<title>PLAN STARK Betrieb – Buchcover</title>
<link href="https://fonts.googleapis.com/css2?family=Barlow:wght@400;500;600&family=Barlow+Condensed:ital,wght@0,400;1,400&family=Source+Serif+4:wght@400;600&display=swap" rel="stylesheet">
<style>
  :root{
    --blue:#2e3e9c;
    --green:#8cbf3f;
    --grey-light:#e2e5ec;
    --ink:#333333;
    --white:#ffffff;
    --bg:#ffffff;
  }
  *{margin:0;padding:0;box-sizing:border-box}
  html,body{width:900px;height:1200px;overflow:hidden;background:var(--bg)}
  .stage{position:relative;width:900px;height:1200px}
  .cover{
    position:absolute;top:328px;width:578px;height:750px;
    transform-origin:0 0;transform:scale(0.727);
    overflow:hidden;background:var(--white);
    box-shadow:0 0 10px rgba(0,0,0,.35);
    font-family:"Barlow",sans-serif;color:var(--ink);
  }
  .cover--front{left:20px}
  .cover--back{left:460px}
  .photo{position:absolute}
  .photo--clock{left:0;top:0;width:290px;height:233px;
    background:
      radial-gradient(ellipse 75% 85% at 42% 62%, rgba(244,245,247,.95) 0%, rgba(214,218,225,.8) 38%, rgba(150,158,172,0) 62%),
      linear-gradient(135deg,#d3d7de 0%,#a4adbb 40%,#6f7a8c 70%,#b9c0cb 100%)}
  .photo--calendar{left:302px;top:0;width:276px;height:203px;
    background:
      radial-gradient(ellipse 55% 60% at 35% 78%, rgba(214,160,120,.85) 0%, rgba(214,160,120,0) 70%),
      radial-gradient(ellipse 40% 35% at 48% 22%, rgba(90,100,120,.55) 0%, rgba(90,100,120,0) 70%),
      linear-gradient(160deg,#f4f5f7 0%,#e3e6ec 55%,#c9d0dc 100%)}
  .photo--tablet{left:0;top:548px;width:358px;height:202px;
    background:
      radial-gradient(ellipse 45% 60% at 8% 40%, rgba(255,214,110,.95) 0%, rgba(240,170,80,.6) 40%, rgba(240,170,80,0) 75%),
      radial-gradient(ellipse 50% 45% at 62% 55%, rgba(190,205,225,.9) 0%, rgba(150,170,200,0) 75%),
      linear-gradient(120deg,#e0a060 0%,#b98a6a 30%,#8394ae 60%,#4e5d78 100%)}
  .photo--coffee{left:368px;top:517px;width:210px;height:233px;
    background:
      radial-gradient(ellipse 45% 30% at 55% 72%, rgba(255,255,255,.95) 0%, rgba(255,255,255,0) 80%),
      linear-gradient(170deg,#eef0f3 0%,#d9dbde 45%,#b59e82 75%,#8a6c4e 100%)}
  .green-bar{position:absolute;background:var(--green)}
  .blue-bar{position:absolute;background:var(--blue)}
  .grey-strip{position:absolute;background:var(--grey-light)}
  .panel{position:absolute;left:42px;top:233px;width:536px;height:284px;background:var(--white)}
  .authors{position:absolute;left:302px;top:251px;font-size:14px;font-weight:500;color:#222}
  .contrib{position:absolute;left:302px;top:276px;font-size:10.5px;color:#333}
  .title{position:absolute;font-family:"Source Serif 4",serif;line-height:1}
  .title__line1{font-size:60px;font-weight:400;letter-spacing:-1px;color:var(--ink)}
  .title__line1 .accent{color:var(--blue)}
  .title__line2{font-size:33px;font-weight:600;color:var(--ink)}
  .cover--front .title{left:84px;top:318px}
  .cover--front .title__line2{margin-left:144px;margin-top:-8px}
  .subtitle{position:absolute;text-align:center;font-size:14px;line-height:24px}
  .cover--front .subtitle{left:42px;width:480px;top:424px;color:var(--green)}
  .badge{position:absolute;left:319px;top:495px;width:124px;height:124px;border-radius:50%;background:var(--green);
    color:var(--white);font-weight:600;font-size:14px;line-height:19px;text-align:center;display:flex;align-items:center;justify-content:center;transform:rotate(-8deg)}
  /* back */
  .back-head{position:absolute;left:0;top:0;width:578px;height:185px;background:var(--grey-light)}
  .cover--back .title{left:80px;top:48px}
  .cover--back .title__line2{margin-left:128px;margin-top:-8px}
  .cover--back .subtitle{left:40px;width:500px;top:140px;color:var(--ink);font-size:13px;line-height:22px}
  .photo--hand{left:335px;top:203px;width:210px;height:110px;
    background:
      radial-gradient(ellipse 30% 45% at 20% 55%, rgba(235,200,180,.8) 0%, rgba(235,200,180,0) 75%),
      linear-gradient(120deg,#d5dee8 0%,#8ea6bd 40%,#58728e 75%,#3e5670 100%)}
  .blurb{position:absolute;left:43px;top:265px;width:252px;font-family:"Barlow Condensed",sans-serif;font-size:9.4px;line-height:14px;text-align:justify;color:#222;hyphens:auto}
  .blurb p+p{margin-top:14px}
  .quote{position:absolute;left:335px;width:208px;font-family:"Barlow Condensed",sans-serif;font-size:9.4px;line-height:14px;color:#222;hyphens:auto}
  .quote__text{font-style:italic}
  .quote__source{color:var(--blue);margin-top:2px}
  .quote--one{top:334px}
  .quote--two{top:494px}
  .footer{position:absolute;left:0;top:645px;width:578px;height:105px;background:var(--blue)}
  .ean{position:absolute;left:412px;top:12px;width:120px;height:46px;background:var(--grey-light);font-size:13px;color:#222;display:flex;align-items:flex-end;justify-content:center;padding-bottom:4px}
  .price{position:absolute;right:58px;top:66px;font-family:"Barlow Condensed",sans-serif;font-size:9px;color:var(--white);word-spacing:2px}
</style>
</head>
<body>
<main class="stage">

  <section class="cover cover--front" aria-label="Vorderseite">
    <div class="photo photo--clock" role="img" aria-label="Foto: Wanduhr vor einer Person im Anzug"></div>
    <div class="photo photo--calendar" role="img" aria-label="Foto: Hand mit Stift über einem Kalender, Smartphone"></div>
    <div class="green-bar" style="left:302px;top:203px;width:276px;height:30px"></div>
    <div class="green-bar" style="left:535px;top:233px;width:43px;height:17px"></div>
    <div class="grey-strip" style="left:0;top:233px;width:42px;height:284px"></div>
    <div class="panel"></div>
    <div class="authors">Dr. Reinhold Kattner, Lothar Brenning</div>
    <div class="contrib">Unter Mitwirkung von Prof. Anton K. Ruhland</div>
    <h1 class="title">
      <div class="title__line1">PLAN <span class="accent">STARK</span></div>
      <div class="title__line2">Betrieb</div>
    </h1>
    <p class="subtitle">Dienstzeiten und Schichtorganisation<br>fair, rentabel und marktnah einrichten</p>
    <div class="blue-bar" style="left:0;top:517px;width:368px;height:31px"></div>
    <div class="photo photo--tablet" role="img" aria-label="Foto: Hände mit Stift an einem Tablet mit Dienstplan"></div>
    <div class="photo photo--coffee" role="img" aria-label="Foto: Kaffeetasse, Zeitung und Tablet auf dem Schreibtisch"></div>
    <div class="badge">Mit vielen<br>Praxis-<br>beispielen</div>
  </section>

  <section class="cover cover--back" aria-label="Rückseite">
    <div class="back-head"></div>
    <h2 class="title">
      <div class="title__line1">PLAN <span class="accent">STARK</span></div>
      <div class="title__line2">Betrieb</div>
    </h2>
    <p class="subtitle">Dienstzeiten und Schichtorganisation<br>fair, rentabel und marktnah einrichten</p>
    <div class="green-bar" style="left:0;top:185px;width:43px;height:48px"></div>
    <div class="green-bar" style="left:0;top:203px;width:325px;height:30px"></div>
    <div class="photo photo--hand" role="img" aria-label="Foto: Hand berührt eine digitale Planungsoberfläche"></div>

    <div class="blurb">
      <p>Die Welt verändert sich dramatisch. Digitalisierung, Fachkräftemangel, Wertewandel und nicht zuletzt Ausnahmezustände wie die Coronakrise stellen Unternehmen vor große Herausforderungen. Wie können Unternehmen flexibel und gleichzeitig wirtschaftlich, kunden- und mitarbeiterorientiert agieren? Reinhold Kattner und Lothar Brenning sehen eine innovative Arbeitszeitgestaltung als entscheidenden Hebel an, um Unternehmen aller Branchen in schnelllebigen Märkten flexibel aufzustellen. Die Autoren beleuchten mit vielen Beispielen aus ihrer Beratungspraxis, warum Arbeitszeitsysteme dringend modernisiert werden müssen und welche Möglichkeiten Sie bereits heute haben, Arbeitszeit innovativ zu gestalten.</p>
      <p>Sie erfahren alles Wissenswerte über klassische Modelle, wie z.B. Schichtplan, Gleitzeit, Vertrauensarbeitszeit, Zeitkontensystem und Teilzeit, über Workforce Management (Workforce Analytics, Personalbedarfsermittlung und Forecast, Personaleinsatzplanung, Zeiterfassung) bis hin zu Lebensarbeitszeit, Gruppenarbeit, Selbstorganisation, Homeoffice und New Work. Dabei lernen Sie nicht nur die Einzelkomponenten kennen, sondern erfahren auch, wie man diese geschickt zu einer für Mitarbeiter und Unternehmen gleichermaßen vorteilhaften Arbeitszeitsystematik kombiniert. Neben diesem strategischen Wissen vermitteln Ihnen die Autoren hilfreiche Methoden zur konkreten operativen Umsetzung dieser Themen.</p>
    </div>

    <blockquote class="quote quote--one">
      <p class="quote__text">„Durch die Weitergabe ihrer umfassenden Erfahrungen aus der Beratung ist es den Autoren in hervorragender Weise gelungen, neue Einsichten und vertieftes Expertenwissen sowohl zur Implementierung von modernen Einsatzplanungs-Lösungen als auch zu konkreten Vorgehensweisen bei der Personaleinsatzplanung zu vermitteln.“</p>
      <p class="quote__source">Anton K. Ruhland, Professor für Personalmanagement an der Hochschule Kessberg</p>
    </blockquote>

    <blockquote class="quote quote--two">
      <p class="quote__text">„Das vorliegende Buch von Kattner und Brenning liefert den entscheidenden Baustein zur Humanisierung von Ökonomie und Unternehmensorganisation und hat das Potenzial zu dem Standardwerk im Thema moderne Arbeitszeitgestaltung und Workforce Management zu werden.“</p>
      <p class="quote__source">Dr. Harald Wenzke, Initiator des Kompetenznetzwerks Fachforum Personal &amp; Top 3 HR Influencer 2020 (HR Rundschau)</p>
    </blockquote>

    <div class="footer">
      <div class="ean">EAN-CODE</div>
      <div class="price">€ 00,00 [D] &nbsp;€00,00 [A] &nbsp;&nbsp; ISBN 000-0-0000-0000-0</div>
    </div>
  </section>

</main>
</body>
</html>
```